small business focused on life coaching and helping others "create better tomorrows" needs a website

The Pell R Group needs a website that focuses on life coaching and helping others "create better tomorrows"; This is a sole proprietorship so the focus should be on Marla, who has worn many hats and in an excellent position to help others. It should include 6 pages _ Home, Bio, Services, Book, Media, Contact Us and the logo that was created by Craft Plaza; also include testimonials from 5-6 individuals as well as why one might need these services (see file included)

Target Market(s)

Immigrants who need help navigating American system in the workplace, home or community, immigrant or at-risk students unable to communicate with their immigrant parents (due to language or unfamiliarity with the new culture) but would share with someone they trust, those in need of a mentor or help with career advancement or choices, those in need of help with public speaking or leadership development - Marla is someone who has worn many hats and in a position to help - extensive networking, an immigrant herself, former teacher, community leader, TV talk show host, author, mother, grandmother, etc.

Industry/Entity Type

Business

Coding

Coded - Design and coding required

Number of Pages Required

5+ page

Font styles to use
Sans Serif

Colors
cadf82
add136

Requirements
Must have
• visuals of Marla - present image of competency, caring, professionalism; need to include a 30-second video (in process of being produced) of Marla promoting the services, need to include 5-6 testimonials (which will be sent later). Please see the document that describes the different pages of the website and what should be included. Give the image of Marla's ability to help people GROW into a more productive self
Nice to have
• This is a sole proprietor business and as such, need to have people feel comfortable in who I am - trust is critical and that is why experience and competency should be shown

```html
<!DOCTYPE html>
<html lang="en">
<head>
<meta charset="utf-8">
<title>The Pell R Group</title>
<link href="https://fonts.googleapis.com/css2?family=Montserrat:wght@400;500;600;700&family=Open+Sans:wght@400;700&display=swap" rel="stylesheet">
<style>
:root{
  --green:#a3c51a;
  --green-light:#cadf82;
  --green-deep:#5e7f1b;
  --brand:#6c9a1e;
  --ink:#333;
  --muted:#666;
  --quote-faint:#f3f3f0;
  --white:#fff;
  --black:#0a0a0a;
  --grey:#d8d8d8;
  --icon-bg:#3b3b3b;
}
*{margin:0;padding:0;box-sizing:border-box}
html,body{width:1200px;height:2281px;overflow:hidden;background:var(--white)}
body{position:relative;font-family:'Montserrat',sans-serif;color:var(--ink)}
.abs{position:absolute}

.site-header{left:0;top:0;width:1200px;height:43px;background:var(--white);border-bottom:1px solid #ddd;z-index:3}
.brand{left:98px;top:9px;font-size:21px;font-weight:500;color:var(--brand);white-space:nowrap}
.main-nav{right:110px;top:14px;display:flex;gap:33px;font-size:13px;color:#222}

.hero{left:0;top:43px;width:1200px;height:505px}
.hero-photo{position:absolute;inset:0;background:linear-gradient(100deg,#8a8680 0%,#b9b4ac 35%,#cfcac2 60%,#e2ded6 100%);clip-path:polygon(0 0,100% 0,100% 444px,600px 504px,0 444px)}
.hero-panel{left:569px;top:170px;width:473px;height:236px;background:rgba(40,40,40,.78);text-align:center;color:var(--white)}
.hero-panel h1{font-family:'Open Sans',sans-serif;font-weight:700;font-size:43px;margin-top:10px;letter-spacing:.5px;line-height:54px}
.hero-panel p{font-size:20px;line-height:26px}
.hero-panel .lead{margin-bottom:20px}
.btn-read{display:inline-block;margin-top:18px;background:var(--green);color:#222;font-size:12px;font-weight:500;padding:9px 17px;border:1px solid #c8e27a}
.slide-arrow{width:38px;height:38px;display:flex;align-items:center;justify-content:center}
.slide-arrow.prev{left:99px;top:208px;background:rgba(255,255,255,.75)}
.slide-arrow.next{left:1062px;top:208px;background:var(--green)}
.scroll-badge{left:572px;top:532px;width:56px;height:56px;border-radius:50%;background:var(--green);border:3px solid var(--white);display:flex;align-items:center;justify-content:center;z-index:2}

.video-back1{left:122px;top:628px;width:406px;height:297px;background:var(--grey)}
.video-back2{left:99px;top:695px;width:403px;height:294px;background:var(--grey)}
.video{left:111px;top:642px;width:403px;height:335px;background:linear-gradient(135deg,#3a3330,#6b5d55 50%,#2d2a28);border:1px solid #999}
.play{left:269px;top:766px}

.needs{left:610px;top:644px;list-style:none;font-size:12.8px;color:#222;width:560px}
.needs li{position:relative;padding-left:26px;line-height:20px;margin-bottom:21px}
.needs li::before{content:"";position:absolute;left:3px;top:6px;width:8px;height:8px;border-radius:50%;background:var(--green)}

.business{left:0;top:1031px;width:1200px;height:394px}
.business-text{position:absolute;left:0;top:0;width:589px;height:394px;background:var(--green)}
.business-photo{position:absolute;left:589px;top:0;width:611px;height:394px;background:linear-gradient(160deg,#5b4a40,#8c6d5a 45%,#3b3a4a)}
.section-title{display:flex;align-items:center;gap:14px;font-weight:700}
.section-title .bar{display:inline-block;width:12px;height:34px;background:var(--green-deep)}
.business .section-title{position:absolute;left:99px;top:42px;font-size:26px;color:var(--white)}
.business-text p{position:absolute;left:100px;top:116px;width:432px;font-size:12px;line-height:20.4px;color:var(--white)}

.testimonials-title{left:0;top:1466px;width:1200px;justify-content:center;font-size:26px;color:var(--green)}
.quote-card{left:160px;top:1542px;width:880px;height:154px;border:1.5px solid #c3da70;border-radius:16px}
.quote-card p{position:absolute;left:24px;top:38px;width:830px;font-size:12.6px;line-height:21px;color:var(--muted);z-index:1}
.quote-mark{position:absolute;left:368px;top:-10px;font-family:'Open Sans',sans-serif;font-size:220px;font-weight:700;color:var(--quote-faint);line-height:1}
.quote-author{position:absolute;right:24px;bottom:12px;font-size:15px;font-weight:600;color:var(--green);display:flex;align-items:center;gap:12px}
.quote-author::before{content:"";width:44px;height:1.5px;background:var(--green)}
.quote-arrow{width:36px;height:41px;background:var(--green);display:flex;align-items:center;justify-content:center}

.contact{left:0;top:1739px;width:1200px;height:492px;background:var(--green)}
.contact .section-title{position:absolute;left:0;top:42px;width:1200px;justify-content:center;font-size:26px;color:var(--white)}
.contact .section-title .bar{background:var(--white)}
.label{font-size:14px;font-weight:700;color:#3a4a10}
.field{background:var(--white);border:1px solid #ccc;font-size:13px;font-style:italic;color:#555;padding:9px 24px}
.send{left:99px;top:415px;width:102px;height:35px;background:var(--green-light);border:1px solid #e3efbd;font-size:13px;font-weight:600;color:#333;display:flex;align-items:center;justify-content:center}
.info-row{display:flex;gap:21px;align-items:flex-start;color:var(--white);font-size:12.5px;line-height:20px}
.info-icon{flex:none;width:31px;height:28px;background:var(--icon-bg);display:flex;align-items:center;justify-content:center}
.social{width:38px;height:36px;background:var(--white)}
.to-top{left:1063px;top:2182px;width:38px;height:38px;border-radius:50%;background:#3a3a3a;display:flex;align-items:center;justify-content:center}

.site-footer{left:0;top:2231px;width:1200px;height:50px;background:var(--black);color:var(--white);font-size:13px;text-align:center;line-height:50px}
</style>
</head>
<body>

<header class="abs site-header">
  <div class="abs brand">The Pell R Group</div>
  <nav class="abs main-nav"><span>Home</span><span>Bio</span><span>Services</span><span>Book</span><span>Media</span><span>Contact Us</span></nav>
</header>

<section class="abs hero">
  <div class="hero-photo" role="img" aria-label="Photo of Marla seated beside a client in an office"></div>
  <div class="abs slide-arrow prev"><svg width="14" height="20" viewBox="0 0 14 20"><path d="M11 2 3 10l8 8" fill="none" stroke="#555" stroke-width="2"/></svg></div>
  <div class="abs hero-panel">
    <h1>WHAT YOU DO</h1>
    <p class="lead">Tell customers more about you.</p>
    <p>Add a few words and a stunning pic to<br>grab their attention and get them to click</p>
    <span class="btn-read">Read More</span>
  </div>
  <div class="abs slide-arrow next"><svg width="14" height="20" viewBox="0 0 14 20"><path d="M3 2l8 8-8 8" fill="none" stroke="#fff" stroke-width="2.5"/></svg></div>
</section>
<div class="abs scroll-badge"><svg width="22" height="14" viewBox="0 0 22 14"><path d="M2 2l9 9 9-9" fill="none" stroke="#fff" stroke-width="3" stroke-linecap="round" stroke-linejoin="round"/></svg></div>

<div class="abs video-back1"></div>
<div class="abs video-back2"></div>
<div class="abs video" role="img" aria-label="Video still of Marla hosting a talk show interview"></div>
<svg class="abs play" width="86" height="86" viewBox="0 0 86 86"><circle cx="43" cy="43" r="22" fill="none" stroke="#fff" stroke-width="3"/><path d="M37 32l15 11-15 11Z" fill="#fff"/></svg>

<ul class="abs needs">
  <li>Are you an immigrant needing help navigating the American system?</li>
  <li>Are you an immigrant parent unable to support your children's career<br>choice or life issue</li>
  <li>Do you need help with your job search?</li>
  <li>Are you considering a career change?</li>
  <li>Are you struggling to balance demands of work, home and life?</li>
  <li>Do you need help with time management, leadership development, etc.?</li>
  <li>Are you worried about your teenager's change in behavior?</li>
  <li>Is your family struggling with an addiction/mental health issue?</li>
</ul>

<section class="abs business">
  <div class="business-text">
    <h2 class="section-title"><span class="bar"></span>Business</h2>
    <p>Life coach (this is a business that is focused on the individual – Marla Venn. As such, need to present Marla as a mature professional with extensive experience in working with people and someone who has been very effective in getting things done. Aside from her personal experience as an immigrant, parent and grandparent, Marla has decades of experience as a teacher and administrator in a number of school systems, Director of a countywide agency, community leader heading a national organization with chapters nationally, talk show host, public speaker/facilitator/emcee, human resource administrator responsible for recruitment and compliance issues, board member for numerous commissions and organizations, etc.</p>
  </div>
  <div class="business-photo" role="img" aria-label="Photo of Marla with two community leaders at an event"></div>
</section>

<h2 class="abs section-title testimonials-title"><span class="bar"></span>TESTIMONIALS</h2>
<div class="abs quote-arrow" style="left:134px;top:1599px"><svg width="14" height="22" viewBox="0 0 14 22"><path d="M11 2 3 11l8 9" fill="none" stroke="#fff" stroke-width="2.5"/></svg></div>
<div class="abs quote-card">
  <span class="quote-mark">&ldquo;</span>
  <p>Marla is my "go-to" person for just about anything. She has been a significant support in my acculturation into western/American culture - helping me navigate the many aspects of life's journey. Through her guidance, I have gained much confidence in myself and in my approach to resolving issues. Her immigrant experience helps her understand my challenges. I cannot thank her enough for alway being there whenever I have needed guidance.</p>
  <span class="quote-author">NORA K</span>
</div>
<div class="abs quote-arrow" style="left:1030px;top:1599px"><svg width="14" height="22" viewBox="0 0 14 22"><path d="M3 2l8 9-8 9" fill="none" stroke="#fff" stroke-width="2.5"/></svg></div>

<section class="abs contact">
  <h2 class="section-title"><span class="bar"></span>CONTACT US</h2>
  <div class="abs label" style="left:99px;top:116px">DROP ME A LINE</div>
  <div class="abs field" style="left:99px;top:146px;width:202px;height:36px">Name</div>
  <div class="abs field" style="left:327px;top:146px;width:202px;height:36px">Email</div>
  <div class="abs field" style="left:557px;top:146px;width:200px;height:36px">Subject</div>
  <div class="abs field" style="left:99px;top:199px;width:658px;height:198px;padding-top:8px">Message</div>
  <div class="abs send">Send</div>

  <div class="abs label" style="left:844px;top:116px">CONTACT ME</div>
  <div class="abs info-row" style="left:844px;top:147px">
    <span class="info-icon"><svg width="10" height="14" viewBox="0 0 10 14"><path d="M5 0a5 5 0 0 0-5 5c0 4 5 9 5 9s5-5 5-9a5 5 0 0 0-5-5Zm0 7a2 2 0 1 1 0-4 2 2 0 0 1 0 4Z" fill="#fff"/></svg></span>
    <span>417 Cedar Hollow Lane<br>Brookfield, Ohio 44403</span>
  </div>
  <div class="abs info-row" style="left:844px;top:193px">
    <span class="info-icon"><svg width="12" height="12" viewBox="0 0 12 12"><path d="M2 0l2 3-1 1.5c1 2 2.5 3.5 4.5 4.5L9 8l3 2-1 2C5 12 0 7 0 1Z" fill="#fff"/></svg></span>
    <span style="line-height:28px;font-size:11.5px">555-204-3391</span>
  </div>
  <div class="abs info-row" style="left:844px;top:234px">
    <span class="info-icon"><svg width="12" height="9" viewBox="0 0 12 9"><path d="M0 0h12v9H0Z" fill="#fff"/><path d="M0 0l6 5 6-5" fill="none" stroke="#3b3b3b"/></svg></span>
    <span style="line-height:28px">marla.venn@example.net</span>
  </div>
  <div class="abs info-row" style="left:844px;top:276px">
    <span class="info-icon"><svg width="12" height="12" viewBox="0 0 12 12"><circle cx="6" cy="6" r="5" fill="none" stroke="#fff" stroke-width="1.5"/><path d="M1 6h10M6 1v10" stroke="#fff" stroke-width="1"/></svg></span>
    <span style="line-height:28px">https://www.thepellrgroup.com</span>
  </div>

  <div class="abs label" style="left:844px;top:335px">FOLLOW US</div>
  <div class="abs social" style="left:844px;top:361px"></div>
  <div class="abs social" style="left:896px;top:361px"></div>
  <div class="abs social" style="left:946px;top:361px"></div>
  <div class="abs social" style="left:998px;top:361px"></div>
</section>

<div class="abs to-top"><svg width="12" height="8" viewBox="0 0 12 8"><path d="M1 7l5-5 5 5" fill="none" stroke="#fff" stroke-width="2"/></svg></div>

<footer class="abs site-footer">Copyright The Pell R Group © 2017 - &nbsp;| All Rights Reserved</footer>

</body>
</html>
```